The Iron Trials Borinquen Coast (ITBC) – Sponsorship Proposal 2026 | Second Edition

We are looking to redesign and elevate our Sponsorship Proposal for the second edition of The Iron Trials Borinquen Coast (ITBC) - a Tactical Fitness competition that combines functional fitness and live-fire shooting in a safe and controlled environment.
The first edition (March 7, 2026) was a proven success, and the updated proposal must reflect that evolution from concept to validated event.
OBJECTIVE
Create a visually striking, premium, and highly structured sponsorship proposal that communicates:
- Credibility (proven event)
- Growth (scaling momentum)
- Experience (not just competition, but a full event)
----------------------------
KEY DATA TO INCLUDE (VERY IMPORTANT)
The design must highlight the following real metrics prominently:
- 96 registered athletes
- 240+ spectators
- 35 volunteers
- 370+ total attendees
- 14 female athletes
- 5 youth participants (ages 12–16)
- $3,300 awarded in prize money
INAUGURAL SPONSORS:
- Coastal Sky Corps
- Caribe Territorial Defense Reserve
- Harbor Militia Auxiliary
- Crestmoor Real Estate
- MTK (Mariposa Trek Kit)
- Quillstone Studio
- Reef Motion 442, KORVA San Juan
- Premier Dispatch PR
- Core Harmony
NEXT EVENT (IMPORTANT FOR DESIGN STORY)
- Event Date: December 19, 2026
- Expected Attendance:
- 130+ athletes
- 300+ spectators
- ~500 total attendees
- Theme: Christmas Experience
- Full event decorated in Christmas theme
- Food vendors + traditional Puerto Rican roasted pork (150+ lbs), community, and sponsor activations
👉 This is NOT just a competition - it is an experience-driven event.
STRUCTURE (BASED ON CURRENT PROPOSAL)
- Use the existing proposal as structural reference , but improve layout, hierarchy, and storytelling:
- Cover Page (modern + bold)
- Executive Summary (UPDATED with real results)
- Event Concept / Experience
- Audience & Attendance (with real + projected numbers)
- Sponsors (social proof section)
- Sponsorship Packages (Alpha = $10,000, Bravo = $1,000, Charlie = $500, Delta = $250)
- Why Sponsor ITBC
- Contact Page
EVENT DIVISIONS (UPDATED – VERY IMPORTANT)
The proposal must clearly showcase the five official competition divisions, with strong visual hierarchy (icons, images, or cards per division). This section should feel dynamic, premium, and easy to scan.
Divisions to include:
SCALE DIVISION (Adaptive)
An adaptive division for those who want to experience ITBC in a controlled environment.
No rankings. No prizes.
This is about completing the challenge.
BEGINNER DIVISION
For athletes ready to compete in a structured and approachable format.
Challenging, but accessible.
Athletes compete for placement.
INTERMEDIATE DIVISION
For athletes with a strong foundation in fitness and shooting.
Heavier loads. Higher standards.
Performance matters.
JÍBARO DIVISION (Elite)
The highest level of competition at ITBC.
Retention holsters required. Rifles carried in slings. Heavier loads.
Built for athletes who want to prove themselves.
MASTERS 45+ DIVISION
For athletes 45+ who want to compete while prioritizing longevity and control.
Maintains competitive intensity within an age-based category.
2-GUN FORMAT (IMPORTANT – INCLUDE BELOW DIVISIONS)
All divisions are available in either:
Pistol
2-Gun (Pistol + Rifle)
In the 2-Gun format, athletes utilize both pistol and rifle throughout the competition, transitioning between weapons under physical fatigue and time pressure.
DESIGN NOTE FOR THIS SECTION
Present divisions as individual visual blocks/cards (like the reference provided)
Use bold titles + short descriptions (keep text tight)
Include action images per division if possible
Highlight Jíbaro Division as the elite tier visually
Ensure this section is one of the most visually engaging pages in the proposal
DESIGN STYLE & VISUAL DIRECTION
We want a military / tactical / premium fitness aesthetic, similar to brands like:
- Brindle Athletics
- The Valor Circuit
- MeshLift-style event decks
Tone:
- Strong
- Clean
- Masculine but modern
- Minimal clutter
COLOR PALETTE (MANDATORY)
Use the following brand colors:
- Light Olive Green (#636B2F)
- Dark Olive Green (#3D4127)
- Sand / Khaki (#C2B280)
- Charcoal / Black (#1C1C1C)
- Light Gray (#D3D3D3)
- White (#FFFFFF)
- Accent Red (#C80018) – for highlights only
DESIGN NOTES
- Use bold typography (military/tactical feel - I will include the font called BOOTCAMP which is the main font used for the first edition)
- Strong use of contrast (dark backgrounds + light text)
- Icons for stats (athletes, spectators, etc.)
- Clean infographics for numbers
- Full-page images for impact (action shots, athletes, shooting, fitness)
- Official logo included (PNG and vectorized)
- Keep it visually dynamic but easy to read
IMPORTANT MESSAGE SHIFT
The proposal must clearly communicate:
- This is NOT a new event
- This is a proven concept that is scaling
Before: “Support us”
Now: “Join a growing movement early”
FINAL DELIVERABLE
- Print-ready PDF (high quality)
- Editable source file (Illustrator)
- Modern, clean layout with strong visual hierarchy
Website: www.theitbc-example.com
Instagram: https://www.instagram.com/theitbc_demo/
- BOOTCAMP

```html
<!DOCTYPE html>
<html lang="en">
<head>
<meta charset="utf-8">
<title>ITBC Sponsorship Proposal</title>
<link href="https://fonts.googleapis.com/css2?family=Bebas+Neue&family=Montserrat:ital,wght@0,400;0,500;0,600;0,700;0,800;1,600&family=Poppins:wght@500;600&display=swap" rel="stylesheet">
<style>
:root{
  --olive:#636B2F;
  --olive-dark:#3D4127;
  --sand:#C2B280;
  --charcoal:#1C1C1C;
  --ink:#141414;
  --gray:#D3D3D3;
  --white:#FFFFFF;
  --red:#C80018;
  --stage-top:#c4c4c4;
  --stage-bottom:#9b9b9b;
}
*{box-sizing:border-box;margin:0;padding:0}
html,body{width:1200px;height:3521px;overflow:hidden}
body{position:relative;background:radial-gradient(ellipse at 50% 40%,var(--stage-top),var(--stage-bottom));font-family:"Montserrat",sans-serif;color:var(--white)}
.page-label{position:absolute;width:447px;text-align:center;font:500 22px "Poppins",sans-serif;color:#f1f1f1}
.deck-title{position:absolute;left:660px;top:300px;font:800 62px/68px "Montserrat",sans-serif;color:#4f4f4f;letter-spacing:-.5px}
.page{position:absolute;width:447px;height:577px;background:var(--ink);overflow:hidden;box-shadow:0 10px 22px rgba(0,0,0,.35)}
.col-left{left:126px}.col-right{left:633px}
.row-1{top:118px}.row-2{top:794px}.row-3{top:1469px}.row-4{top:2145px}.row-5{top:2828px}
.texture{position:absolute;inset:0;background:radial-gradient(circle at 85% 60%,#222 0,#151515 55%)}
.footer{position:absolute;left:0;right:0;bottom:0;height:26px;background:var(--olive);display:flex;align-items:center;justify-content:center;gap:9px;font:500 6.4px "Montserrat",sans-serif;letter-spacing:.1em;color:#ece6cf}
.footer .dot{width:5px;height:5px;border-radius:50%;background:#ece6cf;display:inline-block;margin-right:4px}
.footer .sq{width:5px;height:5px;border:1px solid #ece6cf;display:inline-block;margin-right:4px}
.photo{position:absolute}
.heading{position:absolute;left:34px;top:28px;font:400 25px/1 "Bebas Neue",sans-serif;letter-spacing:.02em;color:var(--white)}
.hl{background:linear-gradient(transparent 58%,var(--red) 58%);padding-right:4px}
.small{font-size:6.3px;line-height:1.45;color:#e6e6e6}
.abs{position:absolute}
.sand{color:var(--sand)}

/* cover */
.cover-photo{inset:0;background:radial-gradient(circle at 25% 30%,#4a4a4a 0,#262626 40%,#111 80%)}
.logo-ring{position:absolute;border-radius:50%;border:2px solid #ddd;display:flex;align-items:center;justify-content:center;text-align:center}
.logo-ring span{font:600 7px/1.3 "Montserrat",sans-serif;color:#eee;letter-spacing:.08em;text-transform:uppercase;width:70%}
.cover-title{position:absolute;left:0;right:0;top:166px;text-align:center;font:400 56px/50px "Bebas Neue",sans-serif;color:var(--white)}
.cover-title .line3{font-size:40px;line-height:44px}
.cover-title .redbox{background:var(--red);padding:0 6px}
.edition{position:absolute;left:0;right:0;top:350px;text-align:center;font:italic 600 15px "Montserrat",sans-serif;letter-spacing:.45em;color:#eee}
.edition b{color:var(--sand);font-style:normal;letter-spacing:2px;margin:0 10px}
.date-block{position:absolute;left:78px;top:412px;width:300px;height:80px;display:flex;align-items:center}
.date-year{font:300 30px "Montserrat",sans-serif;width:86px;text-align:center;border-top:1px solid #ccc;border-bottom:1px solid #ccc;padding:4px 0}
.date-day{width:90px;text-align:center}
.date-day small{display:block;font:600 10px "Montserrat",sans-serif;color:var(--sand);letter-spacing:.05em}
.date-day strong{display:block;font:800 58px/52px "Montserrat",sans-serif;color:var(--sand)}
.date-time{font:500 11px/1.3 "Montserrat",sans-serif;width:86px;text-align:center;border-top:1px solid #ccc;border-bottom:1px solid #ccc;padding:5px 0}
.location{position:absolute;left:0;right:0;top:498px;text-align:center;font:500 8px "Montserrat",sans-serif}

/* stats */
.stat-row{position:absolute;left:34px;width:184px;height:60px;display:flex;align-items:center;gap:8px;border-bottom:1px solid #3a3a3a}
.stat-icon{width:30px;height:30px;flex:none}
.stat-num{font:700 29px/1 "Montserrat",sans-serif;color:var(--sand)}
.stat-lbl{font:500 7.5px/1.2 "Montserrat",sans-serif;text-transform:uppercase}
.stat-lbl small{font-size:5px;color:#bbb}

/* divisions */
.division{position:absolute;left:34px;width:380px;overflow:hidden;background:var(--olive-dark)}
.division .div-photo{position:absolute;top:0;bottom:0;width:52%}
.division .div-text{position:absolute;top:6px;width:50%}
.div-title{font:400 12px "Bebas Neue",sans-serif;color:var(--sand);letter-spacing:.04em;font-style:italic;margin-bottom:3px}
.ticks{list-style:none}
.ticks li{font:500 5.6px/1.45 "Montserrat",sans-serif;color:#eee;padding-left:9px;position:relative}
.ticks li::before{content:"";position:absolute;left:1px;top:1.5px;width:3px;height:5px;border:solid var(--sand);border-width:0 1.2px 1.2px 0;transform:rotate(40deg)}
.division.elite{box-shadow:inset 3px 0 0 var(--red)}

/* sponsors */
.sponsor-box{position:absolute;width:119px;height:132px;border:1px solid #444;background:rgba(30,30,30,.85);display:flex;align-items:center;justify-content:center;text-align:center;padding:6px;font:400 10.5px/1.2 "Bebas Neue",sans-serif;color:#d8d8d8;letter-spacing:.04em}

/* packages */
.pkg-alpha{position:absolute;left:34px;top:70px;width:380px;height:110px;background:#47492c;padding:6px 8px}
.pkg-title{font:400 13px "Bebas Neue",sans-serif;color:var(--sand);letter-spacing:.03em}
.pkg-title em{color:var(--red);font-style:normal}
.pkg-col{position:absolute;top:192px;width:120px;background:#262626;padding:6px}
.inkind{position:absolute;left:163px;top:336px;width:251px;height:50px;background:var(--sand);color:var(--charcoal);padding:5px 8px 5px 30px}
.inkind .ticks li{color:var(--charcoal)}
.inkind .ticks li::before{border-color:var(--charcoal)}
.reasons{position:absolute;left:34px;top:470px;width:380px;height:72px;display:flex;gap:10px}
.reasons-tag{width:26px;background:var(--sand);color:var(--charcoal);display:flex;align-items:center;justify-content:center}
.reasons-tag span{transform:rotate(-90deg);white-space:nowrap;font:400 10px/1 "Bebas Neue",sans-serif;letter-spacing:.05em}

/* back */
.contact-list{position:absolute;left:0;right:0;top:482px;display:flex;flex-direction:column;align-items:center;gap:4px;font:500 6.8px "Montserrat",sans-serif}
.contact-list div{display:flex;align-items:center;gap:5px}
</style>
</head>
<body>

<h1 class="deck-title">ITBC<br>Sponsorship<br>Proposal</h1>

<!-- Cover -->
<div class="page-label col-left" style="top:68px">Cover</div>
<section class="page col-left row-1 cover">
  <div class="photo cover-photo" role="img" aria-label="Athlete in ear protection aiming a rifle on the range, darkened"></div>
  <div class="logo-ring" style="left:171px;top:30px;width:105px;height:105px"><span>The Iron Trials Borinquen Coast</span></div>
  <div class="cover-title">
    THE<br>IRON TRIALS<br><span class="line3"><span class="redbox">BORINQUEN COAST</span> (ITBC)</span>
  </div>
  <div class="edition"><b>////</b>SECOND EDITION<b>////</b></div>
  <div class="date-block">
    <div class="date-year">2026</div>
    <div class="date-day"><small>DECEMBER</small><strong>19</strong></div>
    <div class="date-time">7:30AM to<br>5:00PM</div>
  </div>
  <p class="location"><b>Location:</b> Ridgeline Range Club – Aguas Buenas, Puerto Rico</p>
  <div class="footer"><span><i class="dot"></i>www.theitbc-example.com</span><span>|</span><span><i class="sq"></i>https://www.instagram.com/theitbc_demo/</span></div>
</section>

<!-- Page 1 -->
<div class="page-label col-left" style="top:749px">Page 1</div>
<section class="page col-left row-2">
  <div class="texture"></div>
  <h2 class="heading">EXECUTIVE <span class="hl">SUMMARY</span></h2>
  <p class="abs small" style="left:34px;top:64px;width:380px">The ITBC is the first functional fitness and live-fire competition in the entire Caribbean – a one-of-a-kind event where strength, precision, and adrenaline meet. In a single day, athletes, shooters, and enthusiasts from both worlds will test their endurance, focus, and competitive spirit in a course designed to challenge both physical and mental limits.</p>
  <div class="photo" style="left:34px;top:122px;width:380px;height:225px;background:linear-gradient(160deg,#6f7a63,#3b4235 60%,#2a2e25)" role="img" aria-label="Crowd of athletes gathered for briefing under white event tents"></div>
  <div class="photo" style="left:240px;top:338px;width:174px;height:215px;background:linear-gradient(200deg,#55604a,#2f3328 70%)" role="img" aria-label="Female athlete shooting a pistol at the range"></div>
  <p class="abs small" style="left:34px;top:368px;width:196px;text-align:justify">The 2-Gun option is available in Scale, Beginner, and Intermediate divisions. Athletes competing in 2-Gun will use both a pistol and a rifle during designated stages. Rifle use is integrated in a controlled manner appropriate to each division's difficulty level, with distances and complexity scaled accordingly. All 2-Gun athletes must bring their own rifle and comply with all safety, equipment, and range requirements.</p>
  <p class="abs small" style="left:34px;top:462px;width:196px;text-align:justify">More than just a competition, the ITBC will be an immersive experience where fitness and marksmanship converge with Puerto Rican pride. Participants will run, carry, drag, and shoot under the supervision of certified Range Officers in a safe and controlled environment, with live music, commentators, and an energetic audience.</p>
  <div class="footer"><span><i class="dot"></i>www.theitbc-example.com</span><span>|</span><span><i class="sq"></i>https://www.instagram.com/theitbc_demo/</span></div>
</section>

<!-- Page 2 -->
<div class="page-label col-right" style="top:749px">Page 2</div>
<section class="page col-right row-2">
  <div class="texture"></div>
  <h2 class="heading" style="font-size:22px;line-height:23px">AUDIENCE &amp; ATTEN<span class="hl">DANCE</span><br>(WITH REAL + PROJECTED NUMBERS)</h2>
  <div class="stat-row" style="top:100px"><svg class="stat-icon" viewBox="0 0 30 30"><circle cx="15" cy="15" r="12" fill="none" stroke="#C2B280" stroke-width="1.5"/><path d="M9 16l4 4 8-9" fill="none" stroke="#C2B280" stroke-width="1.5"/></svg><span class="stat-num">96</span><span class="stat-lbl">Registered<br>athletes</span></div>
  <div class="stat-row" style="top:160px"><svg class="stat-icon" viewBox="0 0 30 30"><circle cx="15" cy="15" r="12" fill="none" stroke="#C2B280" stroke-width="1.5"/><circle cx="15" cy="15" r="4" fill="#C2B280"/></svg><div><div class="stat-num">240+</div><div class="stat-lbl">Spectators</div></div></div>
  <div class="stat-row" style="top:220px"><svg class="stat-icon" viewBox="0 0 30 30"><circle cx="15" cy="15" r="12" fill="none" stroke="#C2B280" stroke-width="1.5"/><path d="M15 8v14M8 15h14" stroke="#C2B280" stroke-width="1.5"/></svg><div><div class="stat-num">35</div><div class="stat-lbl">Volunteers</div></div></div>
  <div class="stat-row" style="top:280px"><svg class="stat-icon" viewBox="0 0 30 30"><circle cx="10" cy="15" r="6" fill="none" stroke="#C2B280" stroke-width="1.5"/><circle cx="20" cy="15" r="6" fill="none" stroke="#C2B280" stroke-width="1.5"/></svg><div><div class="stat-num">370+</div><div class="stat-lbl">Total attendees</div></div></div>
  <div class="stat-row" style="top:340px"><svg class="stat-icon" viewBox="0 0 30 30"><circle cx="15" cy="15" r="12" fill="none" stroke="#C2B280" stroke-width="1.5"/><path d="M15 9v12" stroke="#C2B280" stroke-width="1.5"/></svg><span class="stat-num">14</span><span class="stat-lbl">Female<br>athletes</span></div>
  <div class="stat-row" style="top:400px"><svg class="stat-icon" viewBox="0 0 30 30"><rect x="5" y="5" width="20" height="20" fill="none" stroke="#C2B280" stroke-width="1.5"/><path d="M10 15h10" stroke="#C2B280" stroke-width="1.5"/></svg><span class="stat-num">5</span><span class="stat-lbl">Youth <small>(ages 12–16)</small><br>participants</span></div>
  <div class="stat-row" style="top:460px;border-bottom:0"><svg class="stat-icon" viewBox="0 0 30 30"><circle cx="15" cy="15" r="12" fill="none" stroke="#C2B280" stroke-width="1.5"/><path d="M15 7v16M19 11c-1-2-8-2-8 1s8 2 8 5-7 3-8 1" fill="none" stroke="#C2B280" stroke-width="1.4"/></svg><div><div class="stat-num">$3,300</div><div class="stat-lbl">Awarded in prize money</div></div></div>
  <div class="photo" style="left:250px;top:106px;width:167px;height:134px;background:linear-gradient(150deg,#7b7a6a,#45473c)" role="img" aria-label="Athlete aiming a pistol downrange"></div>
  <div class="photo" style="left:250px;top:246px;width:167px;height:134px;background:linear-gradient(150deg,#6c5b52,#3a3632)" role="img" aria-label="Competitor at a shooting station"></div>
  <div class="photo" style="left:250px;top:386px;width:167px;height:136px;background:linear-gradient(150deg,#6f6a4a,#393826)" role="img" aria-label="Athlete performing a physical challenge outdoors"></div>
  <div class="footer"><span><i class="dot"></i>www.theitbc-example.com</span><span>|</span><span><i class="sq"></i>https://www.instagram.com/theitbc_demo/</span></div>
</section>

<!-- Page 3 -->
<div class="page-label col-left" style="top:1416px">Page 3</div>
<section class="page col-left row-3">
  <div class="texture"></div>
  <h2 class="heading">DIVI<span class="hl">SIONS</span></h2>
  <p class="abs small" style="left:34px;top:66px">The competition is divided into five main categories, tailored for all levels:</p>

  <div class="division" style="top:85px;height:76px">
    <div class="div-photo" style="right:0;background:linear-gradient(90deg,#3D4127,#707560 35%,#555a4a)" role="img" aria-label="Group of athletes carrying gear"></div>
    <div class="div-text" style="left:10px"><div class="div-title">SCALE DIVISION (ADAPTIVE)</div><ul class="ticks"><li>An adaptive division for those who want to experience ITBC in a controlled environment.</li><li>No rankings. No prizes.</li><li>This is about completing the challenge.</li></ul></div>
  </div>
  <div class="division" style="top:168px;height:78px">
    <div class="div-photo" style="left:0;background:linear-gradient(270deg,#3D4127,#6a6c60 35%,#4b4d44)" role="img" aria-label="Athlete shooting from the prone position"></div>
    <div class="div-text" style="right:8px;width:46%"><div class="div-title">BEGINNER DIVISION</div><ul class="ticks"><li>For athletes ready to compete in a structured and approachable format.</li><li>Challenging, but accessible.</li><li>Athletes compete for placement.</li></ul></div>
  </div>
  <div class="division" style="top:253px;height:79px">
    <div class="div-photo" style="right:0;background:linear-gradient(90deg,#3D4127,#787566 35%,#57554a)" role="img" aria-label="Female athlete aiming a pistol"></div>
    <div class="div-text" style="left:10px"><div class="div-title">INTERMEDIATE DIVISION</div><ul class="ticks"><li>For athletes with a strong foundation in fitness and shooting.</li><li>Heavier loads. Higher standards.</li><li>Performance matters.</li></ul></div>
  </div>
  <div class="division elite" style="top:339px;height:78px">
    <div class="div-photo" style="left:0;background:linear-gradient(270deg,#3D4127,#6f6a56 35%,#4a473b)" role="img" aria-label="Elite athletes firing rifles on the line"></div>
    <div class="div-text" style="right:8px;width:46%"><div class="div-title">JÍBARO DIVISION (ELITE)</div><ul class="ticks"><li>The highest level of competition at ITBC.</li><li>Retention holsters required. Rifles carried in slings. Heavier loads.</li><li>Built for athletes who want to prove themselves.</li></ul></div>
  </div>
  <div class="division" style="top:424px;height:79px">
    <div class="div-photo" style="right:0;background:linear-gradient(90deg,#3D4127,#8a8c82 35%,#5f6157)" role="img" aria-label="Masters athletes competing near event tents"></div>
    <div class="div-text" style="left:10px"><div class="div-title">MASTERS 45+ DIVISION</div><ul class="ticks"><li>For athletes 45+ who want to compete while prioritizing longevity and control.</li><li>Maintains competitive intensity within an age-based category.</li></ul></div>
  </div>

  <div class="abs" style="left:34px;top:514px;width:380px;display:flex;align-items:center;gap:8px;border-top:1px solid #333;padding-top:4px">
    <span style="font:italic 400 13px 'Bebas Neue',sans-serif;color:var(--sand)">2-GUN FORMAT</span>
    <div><div style="font:600 6px 'Montserrat',sans-serif">ALL DIVISIONS ARE AVAILABLE IN EITHER: &nbsp;✓ PISTOL &nbsp;✓ 2-GUN (PISTOL + RIFLE)</div>
    <div style="font:400 4.8px/1.4 'Montserrat',sans-serif;color:#ccc">In the 2-Gun format, athletes utilize both pistol and rifle throughout the competition, transitioning between weapons under physical fatigue and time pressure.</div></div>
  </div>
  <div class="footer"><span><i class="dot"></i>www.theitbc-example.com</span><span>|</span><span><i class="sq"></i>https://www.instagram.com/theitbc_demo/</span></div>
</section>

<!-- Page 4 -->
<div class="page-label col-right" style="top:1416px">Page 4</div>
<section class="page col-right row-3">
  <div class="texture"></div>
  <div class="photo" style="left:230px;top:0;width:217px;height:551px;background:linear-gradient(90deg,#151515,#3b4656 35%,#2b3038 70%,#1c1c1c)" role="img" aria-label="Shooter in uniform firing a pistol on the range"></div>
  <h2 class="heading">EXPECTED ATTEN<span class="hl">DANCE</span></h2>
  <p class="abs small" style="left:34px;top:66px;width:250px">The Iron Trials Borinquen Coast (ITBC) attracts a highly concentrated audience of active, motivated adults with strong purchasing power and high brand loyalty to companies that support their performance-driven lifestyle.</p>
  <div class="abs" style="left:34px;top:150px;display:flex;gap:14px;align-items:center"><svg width="40" height="44" viewBox="0 0 40 44"><circle cx="20" cy="22" r="17" fill="none" stroke="#C2B280" stroke-width="2"/><path d="M12 23l6 6 11-12" fill="none" stroke="#C2B280" stroke-width="2"/></svg><div><div class="stat-num" style="font-size:34px">130+</div><div style="font:500 19px 'Montserrat',sans-serif">ATHLETES</div></div></div>
  <div class="abs" style="left:34px;top:245px;display:flex;gap:14px;align-items:center"><svg width="40" height="44" viewBox="0 0 40 44"><circle cx="20" cy="22" r="17" fill="none" stroke="#C2B280" stroke-width="2"/><circle cx="20" cy="22" r="6" fill="#C2B280"/></svg><div><div class="stat-num" style="font-size:34px">300+</div><div style="font:500 19px 'Montserrat',sans-serif">SPECTATORS</div></div></div>
  <div class="abs" style="left:34px;top:340px;display:flex;gap:14px;align-items:center"><svg width="40" height="44" viewBox="0 0 40 44"><circle cx="13" cy="22" r="9" fill="none" stroke="#C2B280" stroke-width="2"/><circle cx="27" cy="22" r="9" fill="none" stroke="#C2B280" stroke-width="2"/></svg><div><div style="display:flex;align-items:center;gap:4px"><span class="stat-num" style="font-size:34px">~500</span><span style="font:500 6px 'Montserrat';writing-mode:vertical-rl;transform:rotate(180deg)">TOTAL</span></div><div style="font:500 19px 'Montserrat',sans-serif">ATTENDEES</div></div></div>
  <p class="abs" style="left:34px;top:440px;width:210px;font:500 7.6px/1.35 'Montserrat',sans-serif"><b>Theme:</b> Christmas Experience<br>Full event decorated in Christmas theme<br>Food vendors + traditional Puerto Rican roasted pork (150+ lbs), community, and sponsor activations</p>
  <div class="footer"><span><i class="dot"></i>www.theitbc-example.com</span><span>|</span><span><i class="sq"></i>https://www.instagram.com/theitbc_demo/</span></div>
</section>

<!-- Page 5 -->
<div class="page-label col-left" style="top:2095px">Page 5</div>
<section class="page col-left row-4">
  <div class="texture"></div>
  <h2 class="heading">EVENT LO<span class="hl">CATION</span></h2>
  <p class="abs small" style="left:34px;top:66px;width:380px">Ridgeline Range Club, Aguas Buenas, Puerto Rico. The club spans 17.2 acres, offering exclusive use of the grounds for The Iron Trials Borinquen Coast. The event will occupy the newly leveled field (~90m × 33m) and surrounding trails for running/ruck stages, creating a safe and controlled setting for both physical and shooting challenges.</p>
  <p class="abs small" style="left:34px;top:110px;width:380px">The event area includes the Competition Zone, Spectator Area, Sponsor &amp; Concessions Village, Testing &amp; Prep Field, and Athlete Warm-up Zone, covering 14,537 square meters. The running/ruck course extends over 920 meters, integrated into the site's natural terrain.</p>
  <p class="abs small" style="left:34px;top:150px;width:180px">In essence, sponsors and participants will have full access to the property, transforming it into a stage dedicated to athletic performance, tactical excellence, and brand activation.</p>
  <div class="abs" style="left:34px;top:214px;width:168px;height:98px;background:var(--olive-dark);padding:10px;font:400 17px/17px 'Bebas Neue',sans-serif;color:var(--white)">THIS IS NOT JUST A COMPETITION – IT IS AN EXPERIENCE-DRIVEN EVENT.</div>
  <div class="abs" style="left:224px;top:170px;width:190px;height:142px;border:2px solid #2b9fe0;background:linear-gradient(135deg,#5b6155,#3c4038)" role="img" aria-label="Site plan of the sponsorship village with available and unavailable spaces">
    <span class="abs" style="left:60px;top:60px;font:600 6px 'Montserrat';color:#fff">SPONSORSHIP<br>VILLAGE</span>
    <div class="abs" style="left:6px;top:104px;font:500 4.6px/1.5 'Montserrat';color:#fff">
      <div><i style="display:inline-block;width:5px;height:5px;background:#3fae3f;margin-right:3px"></i>AVAILABLE SPACE</div>
      <div><i style="display:inline-block;width:5px;height:5px;background:var(--red);margin-right:3px"></i>UNAVAILABLE SPACE</div>
      <div><i style="display:inline-block;width:5px;height:5px;background:#e6d12a;margin-right:3px"></i>CHECK-IN AREA</div>
    </div>
  </div>
  <div class="photo" style="left:0;top:327px;width:134px;height:216px;background:linear-gradient(160deg,#5d6352,#2d3028)" role="img" aria-label="Shooter aiming a pistol at the range"></div>
  <div class="photo" style="left:141px;top:327px;width:273px;height:216px;background:linear-gradient(135deg,#3e4a2e,#56603e 50%,#2e3524)" role="img" aria-label="Aerial map of the grounds marking the spectators and competition zones">
    <span class="abs" style="left:85px;top:50px;transform:rotate(-32deg);font:500 15px 'Montserrat';color:#fff">SPECTATORS ZONE</span>
    <span class="abs" style="left:40px;top:130px;transform:rotate(-32deg);font:500 13px 'Montserrat';color:#fff">COMPETITION ZONE</span>
  </div>
  <div class="footer"><span><i class="dot"></i>www.theitbc-example.com</span><span>|</span><span><i class="sq"></i>https://www.instagram.com/theitbc_demo/</span></div>
</section>

<!-- Page 6 -->
<div class="page-label col-right" style="top:2095px">Page 6</div>
<section class="page col-right row-4">
  <div class="texture"></div>
  <h2 class="heading">SPON<span class="hl">SORS</span></h2>
  <div class="sponsor-box" style="left:33px;top:85px">Coastal Sky Corps</div>
  <div class="sponsor-box" style="left:164px;top:85px">Caribe Territorial Defense Reserve</div>
  <div class="sponsor-box" style="left:295px;top:85px">Harbor Militia Auxiliary</div>
  <div class="sponsor-box" style="left:33px;top:230px">Crestmoor Real Estate</div>
  <div class="sponsor-box" style="left:164px;top:230px">MTK (Mariposa Trek Kit)</div>
  <div class="sponsor-box" style="left:295px;top:230px">Quillstone Studio</div>
  <div class="sponsor-box" style="left:33px;top:376px">Reef Motion 442, KORVA San Juan</div>
  <div class="sponsor-box" style="left:164px;top:376px">Premier Dispatch PR</div>
  <div class="sponsor-box" style="left:295px;top:376px">Core Harmony</div>
  <div class="footer"><span><i class="dot"></i>www.theitbc-example.com</span><span>|</span><span><i class="sq"></i>https://www.instagram.com/theitbc_demo/</span></div>
</section>

<!-- Page 7 -->
<div class="page-label col-left" style="top:2778px">Page 7</div>
<section class="page col-left row-5">
  <div class="texture"></div>
  <h2 class="heading">SPONSORSHIP PAC<span class="hl">KAGES</span></h2>
  <div class="pkg-alpha">
    <div style="display:flex;gap:8px;align-items:flex-start">
      <svg width="22" height="24" viewBox="0 0 22 24"><path d="M2 8l9-6 9 6M2 15l9-6 9 6M2 22l9-6 9 6" fill="none" stroke="#e39a2a" stroke-width="3"/></svg>
      <div><div class="pkg-title">ALPHA SPONSOR – <em>$10,000</em> (MAIN SPONSOR – 1 AVAILABLE)</div>
      <div style="font:700 5.6px/1.3 'Montserrat';color:#fff">The premier sponsorship tier. Full brand integration across the entire event, including naming presence in key locations and all major advertising.</div></div>
    </div>
    <div style="display:flex;gap:8px;margin-top:5px">
      <ul class="ticks" style="width:50%"><li>Recognition as "The ITBC – Presented by [Company Name]" in all promotional and press materials.</li><li>Prominent logo on shirts, banners, signage and digital platforms.</li><li>Opportunity for opening ceremony remarks.</li><li>Exclusive 20x20 booth space for brand activation.</li><li>Co-branding on trophies, uniforms and backdrops.</li></ul>
      <ul class="ticks" style="width:50%"><li>Featured presence in social media campaigns and post-event recap video.</li><li>Priority renewal rights for future editions.</li><li>Option to display vehicles, large equipment or installations onsite.</li><li>Inclusion of promotional materials in athlete bags.</li><li>Three complimentary athlete entries.</li></ul>
    </div>
  </div>
  <div class="pkg-col" style="left:34px;height:192px">
    <div style="display:flex;gap:5px"><svg width="16" height="18" viewBox="0 0 16 18"><path d="M1 6l7-4 7 4M1 11l7-4 7 4M1 16l7-4 7 4" fill="none" stroke="#3fae6a" stroke-width="2.4"/></svg><div class="pkg-title" style="font-size:10.5px;line-height:1.05">BRAVO SPONSOR<br><em style="font-size:13px">$1,000</em> <small style="font-size:6px;color:#fff">(UP TO 3 AVAILABLE)</small></div></div>
    <div style="font:400 7.5px/1.05 'Bebas Neue';margin:4px 0">OFFERS SOLID BRAND VISIBILITY AND OPPORTUNITIES FOR ACTIVE PARTICIPATION.</div>
    <ul class="ticks"><li>Logo on athlete shirts, banners and signage.</li><li>Two 10'x10' booth spaces for promotion or sales.</li><li>Recognition on media and social posts.</li><li>Inclusion in event videos and photos.</li><li>Promotional materials in athlete bags.</li><li>Option to sponsor a zone (hydration, recovery or registration).</li><li>One complimentary athlete entry.</li></ul>
  </div>
  <div class="pkg-col" style="left:163px;width:122px;height:136px">
    <div style="display:flex;gap:5px"><svg width="16" height="14" viewBox="0 0 16 14"><path d="M1 6l7-4 7 4M1 12l7-4 7 4" fill="none" stroke="#4fb3a2" stroke-width="2.4"/></svg><div class="pkg-title" style="font-size:10.5px;line-height:1.05">CHARLIE SPONSOR<br><em style="font-size:13px">$500</em> <small style="font-size:6px;color:#fff">(UP TO 10 AVAILABLE)</small></div></div>
    <div style="font:400 7.5px/1.05 'Bebas Neue';margin:4px 0">DESIGNED FOR BRANDS SEEKING EVENT PRESENCE AND DIGITAL PROMOTION AT AN ACCESSIBLE LEVEL.</div>
    <ul class="ticks"><li>Logo on banners, flyers and digital platforms.</li><li>Recognition on media and social posts.</li><li>One 10'x10' activation space.</li><li>Mentions during the event.</li></ul>
  </div>
  <div class="pkg-col" style="left:292px;width:122px;height:136px">
    <div style="display:flex;gap:5px"><svg width="16" height="10" viewBox="0 0 16 10"><path d="M1 8l7-5 7 5" fill="none" stroke="#8f6cc7" stroke-width="2.4"/></svg><div class="pkg-title" style="font-size:10.5px;line-height:1.05">DELTA SPONSOR<br><em style="font-size:13px">$250</em> <small style="font-size:6px;color:#fff">(UNLIMITED)</small></div></div>
    <div style="font:400 7.5px/1.05 'Bebas Neue';margin:4px 0">IDEAL FOR BUSINESSES SEEKING LOCAL AND DIGITAL VISIBILITY WHILE SUPPORTING THE EVENT.</div>
    <ul class="ticks"><li>Logo on sponsor banner and event website.</li><li>Opportunity to distribute brochures, samples or coupons.</li><li>Recognition as Community Sponsor during event announcements.</li></ul>
  </div>
  <div class="inkind">
    <svg class="abs" style="left:8px;top:8px" width="14" height="34" viewBox="0 0 14 34"><rect x="1" y="1" width="12" height="32" fill="none" stroke="#1C1C1C" stroke-width="2"/></svg>
    <div style="font:400 9.5px 'Bebas Neue';letter-spacing:.03em">IN-KIND SPONSORSHIPS – PRODUCT OR SERVICE DONATIONS</div>
    <div style="font:400 5px 'Montserrat';margin-bottom:2px">We welcome in-kind contributions that enhance the event experience or operations.</div>
    <ul class="ticks" style="columns:2"><li>Sports nutrition, hydration or recovery.</li><li>Equipment, tents or gear.</li><li>Media, printing or signage services.</li><li>Professional photography or video.</li></ul>
  </div>
  <h2 class="heading" style="top:412px;font-size:22px">WHY SPONSOR <span class="hl">ITBC</span></h2>
  <p class="abs small" style="left:34px;top:440px;width:380px;font-size:5.6px">The ITBC is more than an event – it is the launch of a new competitive platform for tactical fitness and marksmanship on the island. Sponsoring the inaugural edition gives your brand a permanent place in that story.</p>
  <div class="reasons">
    <div class="reasons-tag"><span>KEY REASONS TO SPONSOR</span></div>
    <ul class="ticks" style="padding-top:4px"><li>First event of its kind in Puerto Rico and the Caribbean.</li><li>Direct access to a disciplined, athletic, service-oriented audience.</li><li>Media and digital exposure before, during, and after the event.</li><li>On-site presence with space for activations, demos, and recruitment.</li><li>Recognition as a founding sponsor in future editions of the competition.</li></ul>
  </div>
  <div class="footer"><span><i class="dot"></i>www.theitbc-example.com</span><span>|</span><span><i class="sq"></i>https://www.instagram.com/theitbc_demo/</span></div>
</section>

<!-- Back -->
<div class="page-label col-right" style="top:2778px">Back</div>
<section class="page col-right row-5">
  <div class="photo" style="inset:0;background:radial-gradient(circle at 50% 35%,#2e2e2e,#161616 70%)" role="img" aria-label="Darkened aerial view of the event grounds"></div>
  <div class="logo-ring" style="left:171px;top:84px;width:105px;height:105px"><span>The Iron Trials Borinquen Coast</span></div>
  <h2 class="heading" style="left:0;right:0;top:350px;text-align:center;font-size:26px">CONTACT <span class="hl">US</span></h2>
  <p class="abs" style="left:70px;top:394px;width:307px;text-align:center;font:400 6.8px/1.45 'Montserrat',sans-serif">We invite you to join us in this inaugural edition and help us build a new tradition of athletic excellence, tactical preparedness, and community engagement in Puerto Rico.</p>
  <div class="contact-list">
    <div><svg width="7" height="9" viewBox="0 0 7 9"><path d="M3.5 8.5S1 5.5 1 3.5a2.5 2.5 0 015 0c0 2-2.5 5-2.5 5z" fill="#C2B280"/></svg>PO BOX 000123 | San Juan, PR 00900</div>
    <div><svg width="8" height="8" viewBox="0 0 8 8"><path d="M1.5 1h1.5l.8 2-1 .8a5 5 0 001.9 1.9l.8-1 2 .8V7A.8.8 0 016 8 6 6 0 010 2a.8.8 0 011-.8z" fill="#C2B280"/></svg>555-010-0650</div>
    <div><svg width="8" height="8" viewBox="0 0 8 8"><circle cx="4" cy="4" r="3.3" fill="none" stroke="#C2B280"/></svg>www.theitbc-example.com</div>
    <div><svg width="8" height="8" viewBox="0 0 8 8"><rect x=".7" y=".7" width="6.6" height="6.6" fill="none" stroke="#C2B280"/></svg>https://www.instagram.com/theitbc_demo/</div>
  </div>
  <div class="footer" style="height:14px"></div>
</section>

</body>
</html>
```